Business Card Design

We recently had a new logo designed by Pixel Harbor. Now we want to create new business cards and letterhead that compliment our new logo.

We are audiologists in private practice specializing in hearing evaluations and fitting hearing aids. We want a clean and professional card.

We need business cards for each audiologist. The names and titles are:
Marnie Ostrova, AuD
Audiologist

Jen Tarbel, AuD
Audiologist

Corvina Plesk, AuD
Audiologist

We also need a business card with no provider. Just a generic one.

Finally, we need an appointment card. This is what the front desk uses to give to the patient with their next appointment date and time.

Target Market(s)

Our clients tend to be highly educated. They are older so the cards should be clean and easy to read. No squirrely font please.

Industry/Entity Type

Business

Contact Information for Business Card

20731 8th Ave NE, suite 417
Seattle, WA 98177
206-592-8074

Requirements
Must have
• Clean
Easy to read
Professional
Modern but approachable / warm
Should not have
• Other pictures besides the logo

```html
<!DOCTYPE html>
<html lang="en">
<head>
<meta charset="utf-8">
<title>Larkfield Hearing Services – Appointment Card</title>
<link href="https://fonts.googleapis.com/css2?family=Open+Sans:wght@400;600;700&display=swap" rel="stylesheet">
<style>
  :root {
    --page-bg: #ecebe8;
    --card-white: #ffffff;
    --card-mist: #dcdcdc;
    --navy: #1b4468;
    --navy-deep: #163a5a;
    --name-blue: #1f4a6e;
    --ink: #2f3a44;
    --white: #ffffff;
    --rule: rgba(255,255,255,0.75);
  }
  * { box-sizing: border-box; margin: 0; padding: 0; }
  html, body {
    width: 1200px; height: 1200px; overflow: hidden;
    background: var(--page-bg);
    font-family: "Open Sans", sans-serif;
  }
  .stage {
    width: 1200px; height: 1200px;
    display: flex; align-items: center; justify-content: center;
  }
  .card {
    position: relative;
    width: 1000px; height: 572px;
    background: var(--navy);
    box-shadow: 0 10px 30px rgba(0,0,0,0.18);
    overflow: hidden;
  }
  .card-top {
    position: absolute; left: 0; top: 0; right: 0; height: 262px;
    background: radial-gradient(ellipse at 40% 70%, var(--card-white) 0%, #f3f3f3 55%, var(--card-mist) 100%);
  }
  .card-bottom {
    position: absolute; left: 0; top: 262px; right: 0; bottom: 0;
    background: linear-gradient(180deg, var(--navy) 0%, var(--navy-deep) 100%);
    color: var(--white);
  }
  .brand {
    position: absolute; left: 60px; top: 118px;
    display: flex; align-items: center; gap: 20px;
  }
  .brand-dot {
    width: 92px; height: 92px; border-radius: 50%;
    background: var(--navy);
  }
  .brand-name {
    font-size: 34px; font-weight: 600; line-height: 1.1;
    color: var(--ink); letter-spacing: 1px; text-transform: uppercase;
  }
  .provider {
    position: absolute; left: 620px; top: 62px;
  }
  .provider-name {
    font-size: 33px; font-weight: 700; color: var(--name-blue);
  }
  .provider-title {
    font-size: 24px; font-weight: 400; color: var(--ink); margin-top: 2px;
  }
  .appt-heading {
    position: absolute; left: 0; right: 0; top: 36px;
    text-align: center; font-size: 30px; font-weight: 700; letter-spacing: 0.5px;
  }
  .appt-date {
    position: absolute; left: 90px; top: 110px;
    display: flex; align-items: flex-end; gap: 14px;
  }
  .appt-time {
    position: absolute; left: 560px; top: 100px;
    display: flex; align-items: flex-end; gap: 14px;
  }
  .icon { width: 44px; height: 44px; flex: none; }
  .fill-line {
    border-bottom: 2px dotted var(--rule);
    height: 30px;
  }
  .fill-line.date { width: 300px; }
  .fill-line.time { width: 130px; position: relative; }
  .fill-line.time span {
    position: absolute; right: -4px; bottom: -22px;
    font-size: 12px; color: var(--rule);
  }
  .address {
    position: absolute; left: 0; right: 0; bottom: 52px;
    text-align: center; font-size: 25px; font-weight: 400;
  }
</style>
</head>
<body>
<main class="stage">
  <article class="card appointment-card">
    <header class="card-top">
      <div class="brand">
        <div class="brand-dot"></div>
        <div class="brand-name">Larkfield<br>Hearing Services</div>
      </div>
      <div class="provider">
        <div class="provider-name">Marnie Ostrova, AuD</div>
        <div class="provider-title">Audiologist</div>
      </div>
    </header>
    <section class="card-bottom">
      <h2 class="appt-heading">NEXT APPOINTMENT</h2>
      <div class="appt-date">
        <svg class="icon" viewBox="0 0 44 44" aria-hidden="true">
          <rect x="5" y="8" width="34" height="31" rx="3" fill="none" stroke="#fff" stroke-width="2.5"/>
          <line x1="5" y1="16" x2="39" y2="16" stroke="#fff" stroke-width="2.5"/>
          <line x1="13" y1="4" x2="13" y2="11" stroke="#fff" stroke-width="2.5"/>
          <line x1="31" y1="4" x2="31" y2="11" stroke="#fff" stroke-width="2.5"/>
          <g fill="#fff">
            <rect x="10" y="21" width="5" height="4"/><rect x="19" y="21" width="5" height="4"/><rect x="28" y="21" width="5" height="4"/>
            <rect x="10" y="29" width="5" height="4"/><rect x="19" y="29" width="5" height="4"/><rect x="28" y="29" width="5" height="4"/>
          </g>
        </svg>
        <div class="fill-line date"></div>
      </div>
      <div class="appt-time">
        <svg class="icon" viewBox="0 0 44 44" aria-hidden="true">
          <circle cx="22" cy="22" r="18" fill="none" stroke="#fff" stroke-width="3"/>
          <polyline points="22,11 22,22 30,28" fill="none" stroke="#fff" stroke-width="3" stroke-linecap="round"/>
        </svg>
        <div class="fill-line time"><span>a.m.</span></div>
        <div class="fill-line time"><span>p.m.</span></div>
      </div>
      <p class="address">20731 8th Ave NE, suite 417 Seattle, WA 98177 206-592-8074</p>
    </section>
  </article>
</main>
</body>
</html>
```